4.25" x 11" Door Hanger Design - Cable Quick Internet Service

We are sourcing a door hanger that will be used to micro target specific neighborhoods with our new "Cable Quick" internet service offering

This will be used as a template for a new type of plan we are offering in very specific areas. The first will be "Willow Hollow" with 3 plan offerings.

Stock photos should be family friendly but we want something modern and exciting that we can use to advertise a new internet service offering.
Updates

Sorry if I missed this before, but we would of course like our website and phone number with an encouragement to call us Website: www.brandovex.example Phone: 555-203-4187

Target Market(s)

Residential Internet Service

Industry/Entity Type

Internet Service Provider

Font styles to use
Sans Serif
Other font styles liked:
• RockoFLF

Colors

Designer to choose colors to be used in the design.

Requirements
Must have
• 1) Our logo with "Internet Services" nearby to show "Brandovex Internet Services" (name and what we do)
• 2) "Cable Quick Internet Service is Now Available in Willow Hollow!"
• 3) Show three plans, we don't know the price yet and we will edit the winning design eventually when we know the exact price.
• 100 Mbps $XX.XX per month
• 250 Mbps $XX.XX per month
• 1 Gbps $XX.XX per month
• 4) The plan names and prices should be easy to edit in the future if/when we try these in different markets.
• This ad will be modified with specific information like prices and the location when we use it in specific spots.
• We will be using Quikprintova for the printing, please use their website for the punch hole location, dimensions, etc.
• https://www.quikprintova.example/door-hanger-printing/
Nice to have
• We want to demonstrate far higher than normal internet service speed offerings. This can use whatever you think demonstrates this idea to the customers better, something like a speed test looking logo
Should not have
• Do not copy our website, we want a fresh design

```html
<!DOCTYPE html>
<html lang="en">
<head>
<meta charset="utf-8">
<title>Brandovex Door Hanger – Cable Quick Internet Service</title>
<link href="https://fonts.googleapis.com/css2?family=Roboto:wght@300;400;500&family=Lato:wght@400;700&family=Oswald:wght@400&display=swap" rel="stylesheet">
<style>
  :root{
    --brand-blue:#2188cf;
    --ink:#2b2b2b;
    --band-grey:#d6d7d9;
    --footer-grey:#636466;
    --paper:#ffffff;
    --page:#ffffff;
  }
  *{margin:0;padding:0;box-sizing:border-box}
  html,body{width:1200px;height:1200px;overflow:hidden;background:var(--page)}
  .canvas{position:relative;width:1200px;height:1200px}
  .door-hanger{
    position:absolute;left:397px;top:72px;width:407px;height:1054px;
    background:var(--paper);overflow:hidden;
    font-family:"Roboto",Arial,sans-serif;color:var(--ink);
  }
  .hero-photo{
    position:absolute;left:0;top:0;width:407px;height:442px;
    background:linear-gradient(180deg,#f4f4f2 0%,#ecebe8 45%,#c9d7e6 75%,#a9bdd3 100%);
  }
  .die-cut{position:absolute;left:0;top:0;width:407px;height:200px}
  .rule-blue{position:absolute;left:0;width:407px;background:var(--brand-blue)}
  .rule-top{top:442px;height:5px}
  .brand{
    position:absolute;top:470px;left:0;width:407px;
    display:flex;justify-content:center;align-items:center;gap:10px;
  }
  .brand-mark{width:16px;height:16px;border-radius:50%;background:var(--brand-blue)}
  .brand-name{font-weight:300;font-size:46px;line-height:1;color:var(--brand-blue);letter-spacing:-1px}
  .brand-tagline{position:absolute;top:524px;left:0;width:407px;text-align:center;font-size:22px;font-weight:400}
  .accent{color:var(--brand-blue)}
  .headline{position:absolute;left:0;width:407px;text-align:center;font-weight:500;white-space:nowrap}
  .headline-1{top:577px;font-size:25px}
  .headline-2{top:608px;font-size:25px}
  .headline-3{top:638px;font-size:40px;color:var(--brand-blue);letter-spacing:-0.5px}
  .offer-title{position:absolute;top:717px;left:0;width:407px;text-align:center;font-size:22px;font-weight:500;letter-spacing:0.5px}
  .plans-band{position:absolute;top:790px;left:0;width:407px;height:136px;background:var(--band-grey)}
  .plan{position:absolute;top:768px;width:120px;margin-left:-60px;text-align:center}
  .plan-icon{display:block;margin:0 auto;width:56px;height:48px}
  .plan-speed{margin-top:16px;font-family:"Oswald",sans-serif;font-size:22px;line-height:27px;color:#333}
  .plan-price{font-family:"Oswald",sans-serif;font-size:22px;line-height:27px;color:var(--brand-blue)}
  .plan-term{font-family:"Lato",sans-serif;font-size:16px;line-height:22px}
  .info-lead{position:absolute;top:947px;left:0;width:407px;text-align:center;font-family:"Lato",sans-serif;font-size:18px;font-weight:700}
  .rule-bottom{top:975px;height:6px}
  .contact-bar{
    position:absolute;top:981px;left:0;width:407px;height:73px;background:var(--footer-grey);
    color:#fff;font-family:"Lato",sans-serif;font-weight:700;font-size:15px;
    display:flex;justify-content:center;align-items:center;gap:30px;white-space:nowrap;
  }
  .contact-divider{font-weight:400}
</style>
</head>
<body>
<div class="canvas">
  <div class="door-hanger">
    <div class="hero-photo" role="img" aria-label="Photo of a smiling family of four gathered around a laptop at home"></div>
    <svg class="die-cut" viewBox="0 0 407 200" aria-hidden="true">
      <defs>
        <radialGradient id="holeShade" cx="50%" cy="45%" r="55%">
          <stop offset="0" stop-color="#d4d4d4"/>
          <stop offset="1" stop-color="#bdbdbd"/>
        </radialGradient>
      </defs>
      <line x1="146" y1="0" x2="179" y2="62" stroke="#b8b8b8" stroke-width="2"/>
      <circle cx="203" cy="118" r="59" fill="url(#holeShade)"/>
    </svg>
    <div class="rule-blue rule-top"></div>

    <div class="brand">
      <span class="brand-mark"></span>
      <span class="brand-name">Brandovex</span>
    </div>
    <div class="brand-tagline">Internet <span class="accent">Services</span></div>

    <div class="headline headline-1"><span class="accent">Cable Quick</span> Internet Service</div>
    <div class="headline headline-2">IS NOW <span class="accent">AVAILABLE IN</span></div>
    <div class="headline headline-3">WILLOW HOLLOW!</div>

    <div class="offer-title"><span class="accent">WE</span> OFFERING :</div>

    <div class="plans-band"></div>

    <div class="plan" style="left:77px">
      <svg class="plan-icon" viewBox="0 0 56 48" aria-hidden="true">
        <path d="M1 1h54v34L28 47 1 35z" fill="#2188cf" stroke="#fff" stroke-width="2"/>
        <path d="M15 30a14 14 0 1 1 26 0" fill="none" stroke="#fff" stroke-width="2.5" stroke-linecap="round"/>
        <line x1="28" y1="26" x2="35" y2="15" stroke="#fff" stroke-width="2.5" stroke-linecap="round"/>
      </svg>
      <div class="plan-speed">100MBPS</div>
      <div class="plan-price">$XX.XX</div>
      <div class="plan-term">Per month</div>
    </div>

    <div class="plan" style="left:198px">
      <svg class="plan-icon" viewBox="0 0 56 48" aria-hidden="true">
        <path d="M1 1h54v34L28 47 1 35z" fill="#2188cf" stroke="#fff" stroke-width="2"/>
        <path d="M15 30a14 14 0 1 1 26 0" fill="none" stroke="#fff" stroke-width="2.5" stroke-linecap="round"/>
        <line x1="28" y1="26" x2="35" y2="15" stroke="#fff" stroke-width="2.5" stroke-linecap="round"/>
      </svg>
      <div class="plan-speed">250MBPS</div>
      <div class="plan-price">$XX.XX</div>
      <div class="plan-term">Per month</div>
    </div>

    <div class="plan" style="left:321px">
      <svg class="plan-icon" viewBox="0 0 56 48" aria-hidden="true">
        <path d="M1 1h54v34L28 47 1 35z" fill="#2188cf" stroke="#fff" stroke-width="2"/>
        <path d="M15 30a14 14 0 1 1 26 0" fill="none" stroke="#fff" stroke-width="2.5" stroke-linecap="round"/>
        <line x1="28" y1="26" x2="35" y2="15" stroke="#fff" stroke-width="2.5" stroke-linecap="round"/>
      </svg>
      <div class="plan-speed">1GBPS</div>
      <div class="plan-price">$XX.XX</div>
      <div class="plan-term">Per month</div>
    </div>

    <div class="info-lead"><span class="accent">For more</span> information :</div>
    <div class="rule-blue rule-bottom"></div>
    <div class="contact-bar">
      <span class="contact-phone">( 555 ) 203 4187</span>
      <span class="contact-divider">|</span>
      <span class="contact-web">www.brandovex.example</span>
    </div>
  </div>
</div>
</body>
</html>
```